School District In Need of Powerful Presentation

Create a modern PPT design template -- standard and widescreen -- for the Pell RU-8K school district inspired by its logo. The presentation should be a modern projection of 21st education that excites the people who view it. The school district is located in a rural farming community with a view of the rocky mountains to its west (check out this picture www.campsiteatmarblefork.example/AnimatedImages/HomeGallery/000MountainScene.jpg). People in this community want quality education for their children with opportunities for them to be successful after they graduate.

Target Market(s)

The Harbrook and Denning communities in Northern Colorado

Industry/Entity Type

Education

Font styles to use
Sans Serif

Colors
ec1f27
3176b5
acd036
fece3e
f78f20

Requirements
Must have
• The name of the school district:
• Pell County School District RU-8K Harbrook-Denning
• Website address: www.pellru8k.example/
• Email: listen@pellru8k.example
Nice to have
• A couple of color options including their current color scheme: red, gold, black
• Placeholder for pictures of students and teachers
Should not have
• Please do not use the full logo in it's current for, but you may use elements of the logo.

```html
<!DOCTYPE html>
<html lang="en">
<head>
<meta charset="utf-8">
<title>Design Idea 01c – Individual Slides</title>
<link href="https://fonts.googleapis.com/css2?family=Open+Sans:ital,wght@0,400;0,600;0,700;1,400&family=Roboto+Condensed:wght@700&display=swap" rel="stylesheet">
<style>
:root{
  --red:#ec1f27;--blue:#3176b5;--green:#acd036;--yellow:#fece3e;--orange:#f78f20;
  --purple:#6d4b9e;--teal:#35a9c6;--maroon:#8e0d0d;--ink:#333;--grey:#9a9a9a;
  --sky:#3ba7c8;--royal:#4677c0;--deep:#1f5866;
}
*{margin:0;padding:0;box-sizing:border-box}
html,body{width:1200px;height:1200px;overflow:hidden;background:#000}
.board{position:relative;width:1200px;height:1200px;background:#000;font-family:"Open Sans",sans-serif}
.board-title{position:absolute;top:14px;left:0;width:1200px;text-align:center;font-family:"Roboto Condensed",sans-serif;font-weight:700;font-size:48px;color:#3c3c3c;letter-spacing:1px}
.board-sub{position:absolute;top:78px;left:0;width:1200px;text-align:center;font-family:"Roboto Condensed",sans-serif;font-weight:700;font-size:28px;color:#565656}
.slide{position:absolute;width:393px;height:223px;font-family:"Open Sans",sans-serif}
.c1{left:3px}.c2{left:405px}.c3{left:806px}
.r1{top:139px}.r2{top:381px}.r3{top:622px}.r4{top:862px}
.f-red{fill:var(--red)}.f-blue{fill:var(--blue)}.f-green{fill:var(--green)}.f-yellow{fill:var(--yellow)}
.f-orange{fill:var(--orange)}.f-purple{fill:var(--purple)}.f-teal{fill:var(--teal)}.f-white{fill:#fff}
.f-ink{fill:var(--ink)}.f-grey{fill:var(--grey)}.f-maroon{fill:var(--maroon)}
.s-red{stroke:var(--red)}.s-blue{stroke:var(--blue)}.s-green{stroke:var(--green)}.s-orange{stroke:var(--orange)}
.s-purple{stroke:var(--purple)}.s-teal{stroke:var(--teal)}
.slide-title{font-weight:700;font-size:12px;fill:#fff;text-anchor:middle}
.brand{font-weight:700;font-size:7px;fill:var(--maroon)}
.foot{font-weight:700;font-size:5px;fill:#222}
.h{font-weight:700;font-size:7px;fill:var(--ink)}
.b{font-size:4.4px;fill:var(--grey)}
.w{fill:#fff}
.mid{text-anchor:middle}.end{text-anchor:end}
.tick{fill:none;stroke-width:1.6;stroke-linecap:round;stroke-linejoin:round}
.ring{fill:none;stroke-width:9}
</style>
</head>
<body>
<div class="board">
  <div class="board-title">DESIGN IDEA - 01c</div>
  <div class="board-sub">Individual Slides</div>

  <svg width="0" height="0" style="position:absolute">
    <defs>
      <linearGradient id="bar" x1="0" x2="1"><stop offset="0" stop-color="#6e0707"/><stop offset=".5" stop-color="#b3141a"/><stop offset="1" stop-color="#6e0707"/></linearGradient>
      <linearGradient id="peaks" x1="0" x2="0" y1="0" y2="1"><stop offset="0" stop-color="#d6d6d6"/><stop offset="1" stop-color="#f7f7f7"/></linearGradient>
      <symbol id="hex" viewBox="-33 -33 66 66" overflow="visible"><polygon points="0,-33 28.6,-16.5 28.6,16.5 0,33 -28.6,16.5 -28.6,-16.5"/></symbol>
      <symbol id="chrome" viewBox="0 0 491 279">
        <rect width="491" height="279" fill="#fff"/>
        <rect x="8" y="2" width="84" height="30" fill="url(#peaks)" role="img" aria-label="Mountain range sketch"/>
        <rect x="99" y="2" width="300" height="32" fill="url(#bar)"/>
        <circle cx="446" cy="20" r="4" class="f-red"/>
        <text x="452" y="22.5" class="brand">Pell RU-8K</text>
        <rect x="0" y="250" width="49" height="3" class="f-red"/><rect x="49" y="250" width="49" height="3" class="f-blue"/>
        <rect x="98" y="250" width="49" height="3" class="f-green"/><rect x="147" y="250" width="49" height="3" class="f-yellow"/>
        <rect x="196" y="250" width="49" height="3" class="f-orange"/><rect x="245" y="250" width="49" height="3" class="f-red"/>
        <rect x="294" y="250" width="49" height="3" class="f-blue"/><rect x="343" y="250" width="49" height="3" class="f-green"/>
        <rect x="392" y="250" width="49" height="3" class="f-yellow"/><rect x="441" y="250" width="50" height="3" class="f-orange"/>
        <text x="18" y="268" class="foot">Pell County School District RU-8K Harbrook-Denning</text>
        <circle cx="203" cy="266" r="6" class="f-orange"/><path d="M199.5 266.5 L203 263 L206.5 266.5 V269 H199.5Z" fill="#fff"/>
        <text x="216" y="268" class="foot">Website - www.pellru8k.example</text>
        <circle cx="356" cy="266" r="6" class="f-orange"/><rect x="352.5" y="263.5" width="7" height="5" fill="#fff"/>
        <text x="369" y="268" class="foot">eMail - listen@pellru8k.example</text>
      </symbol>
    </defs>
  </svg>

  <!-- Row 1 -->
  <svg class="slide c1 r1" viewBox="0 0 491 279">
    <use href="#chrome"/>
    <text x="249" y="24" class="slide-title">ENTER YOUR TITLE</text>
    <use href="#hex" x="176" y="51" width="66" height="66" class="f-blue"/>
    <use href="#hex" x="241" y="51" width="66" height="66" class="f-orange"/>
    <use href="#hex" x="145" y="108" width="66" height="66" class="f-purple"/>
    <use href="#hex" x="273" y="108" width="66" height="66" class="f-green"/>
    <use href="#hex" x="176" y="165" width="66" height="66" class="f-red"/>
    <use href="#hex" x="241" y="165" width="66" height="66" class="f-teal"/>
    <circle cx="209" cy="86" r="8" class="w"/><circle cx="274" cy="86" r="8" fill="none" stroke="#fff" stroke-width="2"/>
    <circle cx="178" cy="141" r="9" fill="none" stroke="#fff" stroke-width="2"/><text x="178" y="143.5" class="mid" style="font-size:7px;font-weight:700;fill:#fff">24</text>
    <rect x="296" y="134" width="20" height="12" rx="2" class="w"/>
    <circle cx="209" cy="198" r="9" fill="none" stroke="#fff" stroke-width="2"/><text x="209" y="200.5" class="mid" style="font-size:7px;font-weight:700;fill:#fff">1</text>
    <path d="M264 200 L284 192 L280 198 L286 202Z" class="w"/>
    <circle cx="242" cy="134" r="12" fill="none" stroke="#999" stroke-width="2"/><line x1="230" y1="134" x2="254" y2="134" stroke="#999" stroke-width="1.5"/><line x1="242" y1="122" x2="242" y2="146" stroke="#999" stroke-width="1.5"/>
    <text x="242" y="159" class="mid b" style="font-size:5px">Heading key</text>
    <text x="149" y="76" class="h end">Title Goes Here</text>
    <text x="149" y="86" class="b end">Making it look like readable English.</text><text x="149" y="95" class="b end">Many desktop publishing after</text><text x="149" y="104" class="b end">packages etc</text>
    <text x="121" y="132" class="h end">Title Goes Here</text>
    <text x="121" y="142" class="b end">Making it look like readable</text><text x="121" y="151" class="b end">English. Many desktop publishing</text><text x="121" y="160" class="b end">after packages etc</text>
    <text x="141" y="188" class="h end">Title Goes Here</text>
    <text x="141" y="198" class="b end">Making it look like readable</text><text x="141" y="207" class="b end">English. Many desktop publishing</text><text x="141" y="216" class="b end">after packages etc</text>
    <text x="340" y="71" class="h">Title Goes Here</text>
    <text x="340" y="81" class="b">Making it look like readable English.</text><text x="340" y="90" class="b">Many desktop publishing after</text><text x="340" y="99" class="b">packages etc</text>
    <text x="366" y="127" class="h">Title Goes Here</text>
    <text x="366" y="137" class="b">Making it look like readable</text><text x="366" y="146" class="b">English. Many desktop publishing</text><text x="366" y="155" class="b">after packages etc</text>
    <text x="340" y="186" class="h">Title Goes Here</text>
    <text x="340" y="196" class="b">Making it look like readable</text><text x="340" y="205" class="b">English. Many desktop publishing</text><text x="340" y="214" class="b">after packages etc</text>
  </svg>

  <svg class="slide c2 r1" viewBox="0 0 491 279">
    <use href="#chrome"/>
    <text x="249" y="24" class="slide-title">ENTER YOUR TITLE</text>
    <g stroke="#bbb" stroke-width="1"><line x1="132" y1="137" x2="131" y2="78"/><line x1="132" y1="137" x2="186" y2="119"/><line x1="132" y1="137" x2="165" y2="184"/><line x1="132" y1="137" x2="98" y2="184"/><line x1="132" y1="137" x2="76" y2="119"/></g>
    <circle cx="131" cy="78" r="20" class="f-blue"/><circle cx="186" cy="119" r="20" class="f-green"/>
    <circle cx="165" cy="184" r="20" class="f-purple"/><circle cx="98" cy="184" r="20" class="f-teal"/><circle cx="76" cy="119" r="20" class="f-orange"/>
    <circle cx="132" cy="137" r="23" class="f-red"/>
    <g class="w"><circle cx="131" cy="78" r="7" fill="none" stroke="#fff" stroke-width="1.5"/><rect x="179" y="113" width="14" height="12" fill="none" stroke="#fff" stroke-width="1.5"/><rect x="158" y="179" width="14" height="10"/><rect x="91" y="179" width="14" height="10"/><circle cx="76" cy="119" r="6" fill="none" stroke="#fff" stroke-width="1.5"/></g>
    <text x="132" y="131" class="mid w" style="font-size:4.6px">Department</text><text x="132" y="139" class="mid w" style="font-size:4.6px">of</text><text x="132" y="147" class="mid w" style="font-size:4.6px">Commerce</text>
    <g style="font-size:10px;font-weight:700">
      <rect x="230" y="73" width="22" height="3" class="f-blue"/><text x="271" y="78" class="f-blue">01</text>
      <rect x="230" y="105" width="22" height="3" class="f-green"/><text x="271" y="110" class="f-green">02</text>
      <rect x="230" y="137" width="22" height="3" class="f-purple"/><text x="271" y="143" class="f-purple">03</text>
      <rect x="230" y="167" width="22" height="3" class="f-blue"/><text x="271" y="172" class="f-blue">04</text>
      <rect x="230" y="200" width="22" height="3" class="f-orange"/><text x="271" y="205" class="f-orange">05</text>
    </g>
    <text x="304" y="72" class="h" style="font-size:6px">Your Title</text><text x="304" y="82" class="b">Ipsum generators on the Internet tend to repeat</text><text x="304" y="89" class="b">predefined chunks</text>
    <text x="304" y="104" class="h" style="font-size:6px">Your Title</text><text x="304" y="113" class="b">Ipsum generators on the Internet tend to repeat</text><text x="304" y="120" class="b">predefined chunks</text>
    <text x="304" y="136" class="h" style="font-size:6px">Your Title</text><text x="304" y="145" class="b">Ipsum generators on the Internet tend to repeat</text><text x="304" y="152" class="b">predefined chunks</text>
    <text x="304" y="167" class="h" style="font-size:6px">Your Title</text><text x="304" y="176" class="b">Ipsum generators on the Internet tend to repeat</text><text x="304" y="183" class="b">predefined chunks</text>
    <text x="304" y="198" class="h" style="font-size:6px">Your Title</text><text x="304" y="207" class="b">Ipsum generators on the Internet tend to repeat</text><text x="304" y="214" class="b">predefined chunks</text>
  </svg>

  <svg class="slide c3 r1" viewBox="0 0 491 279">
    <use href="#chrome"/>
    <text x="249" y="24" class="slide-title">INFOGRAPGHIC STYLE TEMPLATE</text>
    <circle cx="119" cy="90" r="34" class="f-red"/><circle cx="165" cy="133" r="34" class="f-blue"/>
    <circle cx="119" cy="176" r="34" class="f-orange"/><circle cx="73" cy="133" r="34" class="f-green"/>
    <circle cx="119" cy="133" r="23" fill="#fff"/>
    <text x="119" y="130" class="mid f-ink" style="font-size:5.5px">Rivalry or-</text><text x="119" y="139" class="mid f-ink" style="font-size:5.5px">Competition</text>
    <rect x="112" y="83" width="14" height="9" rx="1" class="w"/><rect x="160" y="127" width="11" height="12" class="w"/>
    <circle cx="119" cy="181" r="5" class="w"/><circle cx="73" cy="133" r="5" class="w"/>
    <circle cx="260" cy="88" r="17" class="f-blue"/><path d="M254 94 L260 82 L266 94" fill="none" stroke="#fff" stroke-width="2"/>
    <text x="297" y="77" class="h" style="font-size:7.5px">Enter Your Title</text>
    <text x="297" y="88" class="b">Ipsum generators on the Internet tend to repeat</text><text x="297" y="95" class="b">predefined chunks. Ipsum generators on the</text><text x="297" y="102" class="b">Internet tend to repeat predefined chunks</text>
    <circle cx="247" cy="137" r="4" class="f-red"/><text x="256" y="139" class="h" style="font-size:6px">Your Title</text>
    <text x="256" y="147" class="b">Ipsum generators on the</text><text x="256" y="154" class="b">Internet tend to repeat</text><text x="256" y="161" class="b">predefined chunks</text>
    <circle cx="351" cy="137" r="4" class="f-green"/><text x="360" y="139" class="h" style="font-size:6px">Your Title</text>
    <text x="360" y="147" class="b">Ipsum generators on the</text><text x="360" y="154" class="b">Internet tend to repeat</text><text x="360" y="161" class="b">predefined chunks</text>
    <circle cx="247" cy="182" r="4" class="f-purple"/><text x="256" y="184" class="h" style="font-size:6px">Your Title</text>
    <text x="256" y="192" class="b">Ipsum generators on the</text><text x="256" y="199" class="b">Internet tend to repeat</text><text x="256" y="206" class="b">predefined chunks</text>
    <circle cx="351" cy="182" r="4" class="f-teal"/><text x="360" y="184" class="h" style="font-size:6px">Your Title</text>
    <text x="360" y="192" class="b">Ipsum generators on the</text><text x="360" y="199" class="b">Internet tend to repeat</text><text x="360" y="206" class="b">predefined chunks</text>
  </svg>

  <!-- Row 2 -->
  <svg class="slide c1 r2" viewBox="0 0 491 279">
    <use href="#chrome"/>
    <text x="249" y="24" class="slide-title">INFOGRAPGHIC STYLE TEMPLATE</text>
    <g style="font-size:4.8px" class="w">
      <rect x="26" y="64" width="132" height="148" rx="8" class="f-red"/>
      <path d="M92 80 V104 M84 88 H100 M80 98 Q92 110 104 98" stroke="#fff" stroke-width="2.5" fill="none"/><circle cx="92" cy="78" r="3" fill="none" stroke="#fff" stroke-width="2"/>
      <text x="92" y="124" class="mid" style="font-size:8px;font-weight:600">Enter Your Title</text>
      <text x="92" y="149" class="mid">And and prodigiously angelfish one in</text><text x="92" y="161" class="mid">far congenial grotesque leopard</text><text x="92" y="173" class="mid">consider much broke educational spun</text><text x="92" y="185" class="mid">because sheepishly wherever more</text><text x="92" y="197" class="mid">jaguar smooth courteously this.</text>
      <rect x="180" y="64" width="132" height="148" rx="8" class="f-blue"/>
      <circle cx="246" cy="92" r="9" fill="none" stroke="#fff" stroke-width="3"/><path d="M246 79 V105 M233 92 H259" stroke="#fff" stroke-width="2"/>
      <text x="246" y="124" class="mid" style="font-size:8px;font-weight:600">Enter Your Title</text>
      <text x="246" y="149" class="mid">And and prodigiously angelfish one in</text><text x="246" y="161" class="mid">far congenial grotesque leopard</text><text x="246" y="173" class="mid">consider much broke educational spun</text><text x="246" y="185" class="mid">because sheepishly wherever more</text><text x="246" y="197" class="mid">jaguar smooth courteously this.</text>
      <rect x="334" y="64" width="132" height="148" rx="8" class="f-orange"/>
      <path d="M386 100 A14 14 0 1 1 414 100Z" class="w"/><circle cx="400" cy="96" r="3" class="f-orange"/>
      <text x="400" y="124" class="mid" style="font-size:8px;font-weight:600">Enter Your Title</text>
      <text x="400" y="149" class="mid">And and prodigiously angelfish one in</text><text x="400" y="161" class="mid">far congenial grotesque leopard</text><text x="400" y="173" class="mid">consider much broke educational spun</text><text x="400" y="185" class="mid">because sheepishly wherever more</text><text x="400" y="197" class="mid">jaguar smooth courteously this.</text>
    </g>
  </svg>

  <svg class="slide c2 r2" viewBox="0 0 491 279">
    <use href="#chrome"/>
    <text x="249" y="24" class="slide-title">INFOGRAPGHIC STYLE TEMPLATE</text>
    <path d="M107 132 L107 60 A72 72 0 0 1 175.5 109.7Z" class="f-blue"/>
    <path d="M107 132 L175.5 109.7 A72 72 0 0 1 149.3 190.2Z" class="f-red"/>
    <path d="M107 132 L149.3 190.2 A72 72 0 0 1 64.7 190.2Z" class="f-green"/>
    <path d="M107 132 L64.7 190.2 A72 72 0 0 1 38.5 109.7Z" class="f-purple"/>
    <path d="M107 132 L38.5 109.7 A72 72 0 0 1 107 60Z" class="f-teal"/>
    <polygon points="107,100 137.4,122.1 125.8,157.9 88.2,157.9 76.6,122.1" fill="#fff"/>
    <path d="M99 136 L107 128 L115 136 V142 H99Z" class="f-orange"/>
    <g fill="none" stroke="#fff" stroke-width="1.4"><rect x="126" y="82" width="10" height="8"/><rect x="150" y="120" width="9" height="9"/><rect x="139" y="160" width="9" height="10"/><rect x="79" y="170" width="10" height="8"/><rect x="50" y="124" width="10" height="7"/></g>
    <line x1="207" y1="60" x2="207" y2="225" stroke="#e4e4e4"/>
    <rect x="230" y="57" width="20" height="3" class="f-purple"/><rect x="230" y="106" width="20" height="3" class="f-green"/>
    <rect x="230" y="152" width="20" height="3" class="f-blue"/><rect x="230" y="199" width="20" height="3" class="f-orange"/>
    <text x="275" y="59" class="h" style="font-size:6.5px">Enter Your Title</text><text x="275" y="68" class="b">Lorem Ipsum is simply dummy text of the printing and</text><text x="275" y="75" class="b">typesetting industry. Lorem Ipsum has been the industry's</text><text x="275" y="82" class="b">standard dummy text ever since the 1500s.</text>
    <text x="275" y="108" class="h" style="font-size:6.5px">Enter Your Title</text><text x="275" y="117" class="b">Lorem Ipsum is simply dummy text of the printing and</text><text x="275" y="124" class="b">typesetting industry. Lorem Ipsum has been the industry's</text><text x="275" y="131" class="b">standard dummy text ever since the 1500s.</text>
    <text x="275" y="154" class="h" style="font-size:6.5px">Enter Your Title</text><text x="275" y="163" class="b">Lorem Ipsum is simply dummy text of the printing and</text><text x="275" y="170" class="b">typesetting industry. Lorem Ipsum has been the industry's</text><text x="275" y="177" class="b">standard dummy text ever since the 1500s.</text>
    <text x="275" y="202" class="h" style="font-size:6.5px">Enter Your Title</text><text x="275" y="211" class="b">Lorem Ipsum is simply dummy text of the printing and</text><text x="275" y="218" class="b">typesetting industry. Lorem Ipsum has been the industry's</text><text x="275" y="225" class="b">standard dummy text ever since the 1500s.</text>
  </svg>

  <svg class="slide c3 r2" viewBox="0 0 491 279">
    <use href="#chrome"/>
    <text x="249" y="24" class="slide-title">INFOGRAPGHIC STYLE TEMPLATE</text>
    <g class="ring" stroke="#e2e2e2">
      <circle cx="72" cy="134" r="30"/><circle cx="138" cy="134" r="30"/><circle cx="203" cy="134" r="30"/>
      <circle cx="268" cy="134" r="30"/><circle cx="333" cy="134" r="30"/><circle cx="399" cy="134" r="30"/>
    </g>
    <path d="M42 134 A30 30 0 0 1 102 134" class="ring s-blue"/>
    <path d="M108 134 A30 30 0 0 0 168 134" class="ring s-red"/>
    <path d="M173 134 A30 30 0 0 1 233 134" class="ring s-green"/>
    <path d="M238 134 A30 30 0 0 0 298 134" class="ring s-purple"/>
    <path d="M303 134 A30 30 0 0 1 363 134" class="ring s-teal"/>
    <path d="M369 134 A30 30 0 0 0 429 134" class="ring s-orange"/>
    <circle cx="72" cy="134" r="7" class="f-blue"/><circle cx="138" cy="134" r="6" fill="none" stroke="var(--red)" stroke-width="1.5"/>
    <rect x="197" y="129" width="12" height="10" class="f-green"/><polygon points="262,130 274,130 268,140" class="f-purple"/>
    <circle cx="333" cy="134" r="6" class="f-teal"/><path d="M392 141 L404 127 L406 129 L394 143Z" class="f-orange"/>
    <g style="font-size:6.5px;font-weight:600" class="f-ink">
      <text x="138" y="60" class="mid">Idea</text><text x="268" y="60" class="mid">Invent</text><text x="399" y="60" class="mid">Release</text>
      <text x="72" y="189" class="mid">Discover</text><text x="203" y="192" class="mid">Analysis</text><text x="333" y="192" class="mid">Produce</text>
    </g>
    <text x="138" y="73" class="b mid">Lorem Ipsum is simply dummy text of</text><text x="138" y="79" class="b mid">the printing and typesetting industry.</text>
    <text x="268" y="73" class="b mid">Lorem Ipsum is simply dummy text of</text><text x="268" y="79" class="b mid">the printing and typesetting industry.</text>
    <text x="399" y="73" class="b mid">Lorem Ipsum is simply dummy text of</text><text x="399" y="79" class="b mid">the printing and typesetting industry.</text>
    <text x="72" y="197" class="b mid">Lorem Ipsum is simply dummy text of</text><text x="72" y="203" class="b mid">the printing and typesetting industry.</text>
    <text x="203" y="204" class="b mid">Lorem Ipsum is simply dummy text of</text><text x="203" y="210" class="b mid">the printing and typesetting industry.</text>
    <text x="333" y="204" class="b mid">Lorem Ipsum is simply dummy text of</text><text x="333" y="210" class="b mid">the printing and typesetting industry.</text>
  </svg>

  <!-- Row 3 -->
  <svg class="slide c1 r3" viewBox="0 0 491 279">
    <rect width="491" height="279" fill="var(--sky)"/>
    <rect x="150" y="5" width="190" height="150" rx="10" fill="#4fb3d1" role="img" aria-label="Target with arrow in the bullseye before a mountain outline"/>
    <text x="245" y="190" class="mid w" style="font-size:15px;font-weight:700">Define Your Goal</text>
    <text x="245" y="216" class="mid w" style="font-size:4.8px">Bring your business to the next level with powerful presentation material for all business and personal presentation. Suitable for</text>
    <text x="245" y="227" class="mid w" style="font-size:4.8px">all categories business and personal presentation if you are going to use a passage of Lorem Ipsum souffle liquorice bonbon tart</text>
    <text x="245" y="238" class="mid w" style="font-size:4.8px">cookie chocolate cake gummies.</text>
  </svg>

  <svg class="slide c2 r3" viewBox="0 0 491 279">
    <use href="#chrome"/>
    <text x="249" y="24" class="slide-title">ENTER YOUR TITLE</text>
    <text x="18" y="58" class="b" style="font-style:italic;font-size:4.8px">Lorem Ipsum is simply dummy text of the printing and typesetting industry. Lorem Ipsum has been the industry's standard dummy text ever since the 1500s, when an</text>
    <text x="18" y="66" class="b" style="font-style:italic;font-size:4.8px">unknown printer took a galley of type and scrambled it to make a type specimen book.</text>
    <rect x="0" y="114" width="491" height="101" fill="var(--deep)"/>
    <circle cx="77" cy="114" r="20" class="f-red"/><circle cx="189" cy="114" r="20" class="f-green"/>
    <circle cx="301" cy="114" r="20" class="f-orange"/><circle cx="415" cy="114" r="20" class="f-blue"/>
    <g class="w"><rect x="69" y="112" width="3" height="7"/><rect x="74" y="108" width="3" height="11"/><rect x="79" y="105" width="3" height="14"/><rect x="182" y="108" width="14" height="11" rx="2"/><rect x="294" y="107" width="14" height="10" rx="2"/><circle cx="415" cy="114" r="7"/></g>
    <g class="mid w" style="font-size:7px;font-weight:700">
      <text x="77" y="150">Description</text><text x="189" y="150">Description</text><text x="301" y="150">Description</text><text x="415" y="150">Description</text>
    </g>
    <g class="mid" style="font-size:24px;font-weight:700">
      <text x="77" y="182" class="f-red">23%</text><text x="189" y="182" class="f-green">15%</text><text x="301" y="182" class="f-yellow">35%</text><text x="415" y="182" class="f-blue">28%</text>
    </g>
    <g class="mid w" style="font-size:5.5px">
      <text x="77" y="197">Suitable for all category.</text><text x="189" y="197">Suitable for all category.</text><text x="301" y="197">Suitable for all category.</text><text x="415" y="197">Suitable for all category.</text>
    </g>
  </svg>

  <svg class="slide c3 r3" viewBox="0 0 491 279">
    <rect width="491" height="279" fill="var(--royal)"/>
    <rect x="170" y="12" width="150" height="150" rx="75" fill="#5585cb" role="img" aria-label="Gold trophy on a wooden base before a mountain outline"/>
    <text x="245" y="193" class="mid w" style="font-size:14px;font-weight:700">Horay... SUCCESS</text>
    <text x="245" y="218" class="mid w" style="font-size:4.8px">Bring your business to the next level with powerful presentation material for all business and personal presentation. Suitable for</text>
    <text x="245" y="229" class="mid w" style="font-size:4.8px">all categories business and personal presentation if you are going to use a passage of Lorem Ipsum souffle liquorice bonbon tart</text>
    <text x="245" y="240" class="mid w" style="font-size:4.8px">cookie chocolate cake gummies.</text>
  </svg>

  <!-- Row 4 -->
  <svg class="slide c1 r4" viewBox="0 0 491 279">
    <use href="#chrome"/>
    <text x="249" y="24" class="slide-title">ENTER YOUR TITLE</text>
    <text x="18" y="58" class="b" style="font-style:italic;font-size:4.8px">Lorem Ipsum is simply dummy text of the printing and typesetting industry. Lorem Ipsum has been the industry's standard dummy text ever since the 1500s, when an</text>
    <text x="18" y="66" class="b" style="font-style:italic;font-size:4.8px">unknown printer took a galley of type and scrambled it to make a type specimen book.</text>
    <rect x="0" y="85" width="491" height="128" class="f-red"/>
    <rect x="272" y="78" width="209" height="142" class="f-blue"/>
    <text x="49" y="116" class="mid w" style="font-size:5.5px;font-weight:600">Point</text>
    <text x="49" y="144" class="mid w" style="font-size:20px;font-weight:600">9.5</text>
    <text x="49" y="172" class="mid w" style="font-size:4.6px">Lorem ipsum dolor sit</text><text x="49" y="179" class="mid w" style="font-size:4.6px">amet put any thing here</text><text x="49" y="186" class="mid w" style="font-size:4.6px">please be it</text>
    <text x="115" y="117" class="w" style="font-size:5.5px;font-weight:700">ALL TIME REPORT</text>
    <text x="115" y="154" class="w" style="font-size:11px;font-weight:600">25%</text>
    <text x="115" y="172" class="w" style="font-size:4.6px">Lorem ipsum dolor sit amet</text><text x="115" y="179" class="w" style="font-size:4.6px">put any thing here please be</text><text x="115" y="186" class="w" style="font-size:4.6px">it</text>
    <circle cx="232" cy="148" r="22" fill="none" stroke="#fff" stroke-width="7"/>
    <circle cx="232" cy="148" r="22" fill="none" stroke="var(--blue)" stroke-width="7" stroke-dasharray="34.6 139" transform="rotate(-90 232 148)"/>
    <circle cx="232" cy="148" r="15" fill="#333"/><text x="232" y="150" class="mid w" style="font-size:5.5px">5k</text>
    <text x="298" y="117" class="w" style="font-size:5.5px;font-weight:700">ALL TIME REPORT</text>
    <text x="298" y="154" class="w" style="font-size:11px;font-weight:600">65%</text>
    <text x="298" y="172" class="w" style="font-size:4.6px">Lorem ipsum dolor sit amet</text><text x="298" y="179" class="w" style="font-size:4.6px">put any thing here please be</text><text x="298" y="186" class="w" style="font-size:4.6px">it</text>
    <circle cx="433" cy="148" r="22" fill="none" stroke="#fff" stroke-width="7"/>
    <circle cx="433" cy="148" r="22" fill="none" stroke="#1d3f66" stroke-width="7" stroke-dasharray="90 139" transform="rotate(-90 433 148)"/>
    <circle cx="433" cy="148" r="15" fill="#5b97d2"/><text x="433" y="150" class="mid w" style="font-size:5.5px">30k</text>
  </svg>

  <svg class="slide c2 r4" viewBox="0 0 491 279">
    <use href="#chrome"/>
    <text x="249" y="24" class="slide-title">ENTER YOUR TITLE</text>
    <rect x="41" y="58" width="108" height="22" fill="#c9524f"/><rect x="149" y="58" width="73" height="22" class="f-purple"/>
    <rect x="222" y="58" width="72" height="22" class="f-teal"/><rect x="294" y="58" width="72" height="22" class="f-orange"/>
    <rect x="366" y="58" width="73" height="22" fill="#c9524f"/>
    <g class="mid w" style="font-size:5.5px;font-weight:600">
      <text x="95" y="71">Title</text><text x="185" y="71">Regular</text><text x="258" y="71">Medium</text><text x="330" y="71">Premium</text><text x="402" y="71">Super</text>
    </g>
    <g stroke="#bbb" stroke-dasharray="2 2" stroke-width=".6"><line x1="41" y1="105" x2="439" y2="105"/><line x1="41" y1="129" x2="439" y2="129"/><line x1="41" y1="153" x2="439" y2="153"/><line x1="41" y1="177" x2="439" y2="177"/></g>
    <g class="b" style="font-size:5px"><text x="55" y="95">Lorem Ipsum Dolor Sit Amet</text><text x="55" y="119">Lorem Ipsum Dolor Sit Amet</text><text x="55" y="143">Lorem Ipsum Dolor Sit Amet</text><text x="55" y="167">Lorem Ipsum Dolor Sit Amet</text><text x="55" y="191">Lorem Ipsum Dolor Sit Amet</text></g>
    <g class="tick">
      <path d="M181 92 l3 3 l5 -6" class="s-purple"/><path d="M254 92 l3 3 l5 -6" class="s-teal"/><path d="M326 92 l3 3 l5 -6" class="s-orange"/><path d="M398 92 l3 3 l5 -6" class="s-green"/>
      <path d="M181 116 l3 3 l5 -6" class="s-purple"/><path d="M254 116 l3 3 l5 -6" class="s-teal"/><path d="M326 116 l3 3 l5 -6" class="s-orange"/><path d="M398 116 l3 3 l5 -6" class="s-green"/>
      <path d="M254 140 l3 3 l5 -6" class="s-teal"/><path d="M326 140 l3 3 l5 -6" class="s-orange"/><path d="M398 140 l3 3 l5 -6" class="s-green"/>
      <path d="M326 164 l3 3 l5 -6" class="s-orange"/><path d="M398 164 l3 3 l5 -6" class="s-green"/>
      <path d="M398 188 l3 3 l5 -6" class="s-green"/>
    </g>
    <rect x="41" y="199" width="108" height="23" fill="#c9524f"/><rect x="149" y="199" width="73" height="23" class="f-purple"/>
    <rect x="222" y="199" width="72" height="23" class="f-teal"/><rect x="294" y="199" width="72" height="23" class="f-orange"/>
    <rect x="366" y="199" width="73" height="23" fill="#c9524f"/>
    <g class="mid w" style="font-size:9px;font-weight:600">
      <text x="95" y="214">Price</text><text x="185" y="214">32.00$</text><text x="258" y="214">48.00$</text><text x="330" y="214">62.00$</text><text x="402" y="214">78.00$</text>
    </g>
  </svg>

  <svg class="slide c3 r4" viewBox="0 0 491 279">
    <use href="#chrome"/>
    <text x="249" y="24" class="slide-title">ENTER YOUR TITLE</text>
    <g>
      <rect x="36" y="55" width="94" height="178" fill="#fff" stroke="#ddd"/><rect x="36" y="55" width="94" height="67" fill="#e25a4f"/>
      <rect x="144" y="55" width="94" height="178" fill="#fff" stroke="#ddd"/><rect x="144" y="55" width="94" height="67" fill="#8a6bb5"/>
      <rect x="252" y="55" width="94" height="178" fill="#fff" stroke="#ddd"/><rect x="252" y="55" width="94" height="67" fill="#4cb6cf"/>
      <rect x="360" y="55" width="94" height="178" fill="#fff" stroke="#ddd"/><rect x="360" y="55" width="94" height="67" fill="#f59a45"/>
    </g>
    <g class="mid w" style="font-size:5px"><text x="83" y="74">Sub Title</text><text x="191" y="74">Sub Title</text><text x="299" y="74">Sub Title</text><text x="407" y="74">Sub Title</text></g>
    <rect x="75" y="94" width="16" height="11" fill="none" stroke="#fff" stroke-width="2"/><rect x="81" y="105" width="4" height="3" class="w"/>
    <path d="M182 104 L200 92 L195 108 L191 102Z" class="w"/>
    <circle cx="299" cy="100" r="7" fill="none" stroke="#fff" stroke-width="3"/>
    <path d="M407 108 L400 101 A4 4 0 0 1 407 96 A4 4 0 0 1 414 101Z" class="w"/>
    <g class="mid" style="font-size:8px;font-weight:600"><text x="83" y="143" fill="#e25a4f">Title</text><text x="191" y="143" fill="#8a6bb5">Title</text><text x="299" y="143" fill="#4cb6cf">Title</text><text x="407" y="143" fill="#f59a45">Title</text></g>
    <g class="mid b" style="font-size:5px">
      <text x="83" y="182">Lorem ipsum dolor sit amet,</text><text x="83" y="194">consectetur adipiscing elit,</text><text x="83" y="206">sed do eiusmod tempor</text><text x="83" y="218">incididunt ut labore et dolore</text>
      <text x="191" y="182">Lorem ipsum dolor sit amet,</text><text x="191" y="194">consectetur adipiscing elit,</text><text x="191" y="206">sed do eiusmod tempor</text><text x="191" y="218">incididunt ut labore et dolore</text>
      <text x="299" y="182">Lorem ipsum dolor sit amet,</text><text x="299" y="194">consectetur adipiscing elit,</text><text x="299" y="206">sed do eiusmod tempor</text><text x="299" y="218">incididunt ut labore et dolore</text>
      <text x="407" y="182">Lorem ipsum dolor sit amet,</text><text x="407" y="194">consectetur adipiscing elit,</text><text x="407" y="206">sed do eiusmod tempor</text><text x="407" y="218">incididunt ut labore et dolore</text>
    </g>
  </svg>
</div>
</body>
</html>
```